Commercial HVAC and Refrigeration Business cards

Frost-Haven Company is looking for flashy new business cards! We design, install, service and maintain commercial refrigeration, air conditioning, heating and refrigeration equipment. Our colors are blue and white. I'm open to single and double sided designs. Each employee will have their own business card. I've attached a copy of our current logo.

Our website, office and cell phone (cell phone is optional), email address should be clearly legible. "24 Hour Service" and the services we offer are; Sales, Service, Design, Installation, Maintenance. Refrigeration, Heating, Air Conditioning, Ice Machines. Does not have to be in any order.

Target Market(s)

Commercial; Restaurants, hotels, bars, breweries etc.

Industry/Entity Type

Hvac

Contact Information for Business Card

Name; Job Title, Phone Number, Email Address. www.frost-haven-example.com 24 Hour Service. We provide - Sales, Design, Installation, Service, Maintenance. We service - Refrigeration, Heating, Air Conditioning, Ice Machines

Font styles to use
Other font styles liked:
• Be creative

Colors
0255a3
ffffff

Requirements
Must have
• Professional appearance and appeal to commercial clients in the food-service and hospitality industry. Must be clearly legible and easy to understand.
Nice to have
• We want to sell maintenance agreements, perhaps we can use the back of the card to tie into a webpage about our maintenance agreements.
Should not have
• Cartoons or unprofessional. Nothing too edgy.

```html
<!DOCTYPE html>
<html lang="en">
<head>
<meta charset="utf-8">
<title>Frost-Haven Company – Business Cards</title>
<link rel="stylesheet" href="https://fonts.googleapis.com/css2?family=Source+Sans+3:ital,wght@0,400;0,600;0,700;1,700&display=swap">
<style>
  :root {
    --brand-blue: #0255a3;
    --card-blue: #06407f;
    --white: #ffffff;
    --ink-grey: #666a70;
    --ink-dark: #4a4d52;
    --backdrop: #58595b;
  }
  * { box-sizing: border-box; margin: 0; padding: 0; }
  html, body {
    width: 1105px; height: 1200px; overflow: hidden;
    background: var(--backdrop);
    font-family: "Source Sans 3", sans-serif;
  }
  .card {
    position: absolute; left: 218px;
    width: 668px; height: 380px;
    text-align: center;
  }
  .card--front { top: 175px; }
  .card--back { top: 615px; }
  .card-shape { position: absolute; inset: 0; }
  .card-content { position: absolute; inset: 0; }
  .row { position: absolute; left: 0; right: 0; line-height: 1; }

  .company-name { font-weight: 700; font-size: 44px; letter-spacing: 0.5px; }
  .card--front .company-name { color: var(--brand-blue); top: 98px; }
  .card--back .company-name { color: var(--white); top: 80px; }

  .person-name { top: 211px; font-size: 28px; font-weight: 600; color: var(--brand-blue); }
  .person-title { top: 245px; font-size: 21px; color: var(--ink-grey); }
  .contact { font-size: 19px; color: var(--ink-dark); display: flex; justify-content: center; gap: 22px; }
  .contact-line-1 { top: 278px; }
  .contact-line-2 { top: 306px; }
  .contact-item { display: inline-flex; align-items: center; gap: 7px; }
  .contact-icon { width: 17px; height: 17px; fill: var(--brand-blue); }

  .ruled-heading {
    display: flex; align-items: center; justify-content: center; gap: 10px;
    color: var(--white);
  }
  .ruled-heading::before, .ruled-heading::after {
    content: ""; height: 1px; background: rgba(255,255,255,0.75);
  }
  .agreements { top: 200px; font-size: 26px; font-weight: 600; }
  .agreements::before, .agreements::after { width: 125px; }
  .service-list { font-size: 19px; color: var(--white); }
  .service-list .label { font-weight: 700; font-size: 23px; margin-right: 6px; }
  .provide { top: 243px; }
  .service { top: 273px; }
  .around-the-clock { top: 316px; font-size: 18px; font-weight: 700; font-style: italic; }
  .around-the-clock::before, .around-the-clock::after { width: 128px; }
</style>
</head>
<body>

<section class="card card--front" aria-label="Business card front">
  <svg class="card-shape" width="668" height="380" viewBox="0 0 668 380" aria-hidden="true">
    <path d="M30,0 H638 A30,30 0 0 0 668,30 V350 A30,30 0 0 0 638,380 H30 A30,30 0 0 0 0,350 V30 A30,30 0 0 0 30,0 Z" fill="var(--white)"/>
    <path d="M32,4 H636 A30,30 0 0 0 664,32 V348 A30,30 0 0 0 636,376 H32 A30,30 0 0 0 4,348 V32 A30,30 0 0 0 32,4 Z" fill="none" stroke="var(--brand-blue)" stroke-width="4"/>
  </svg>
  <div class="card-content">
    <div class="row company-name">Frost-Haven Company</div>
    <div class="row person-name">Daniel Reyes</div>
    <div class="row person-title">CEO/Founder</div>
    <div class="row contact contact-line-1">
      <span class="contact-item">
        <svg class="contact-icon" viewBox="0 0 24 24" aria-hidden="true"><path d="M6.6 10.8a15 15 0 0 0 6.6 6.6l2.2-2.2a1 1 0 0 1 1-.25 11.4 11.4 0 0 0 3.6.57 1 1 0 0 1 1 1V20a1 1 0 0 1-1 1A17 17 0 0 1 3 4a1 1 0 0 1 1-1h3.5a1 1 0 0 1 1 1c0 1.25.2 2.45.57 3.57a1 1 0 0 1-.25 1z"/></svg>
        555 014 2290
      </span>
      <span class="contact-item">
        <svg class="contact-icon" viewBox="0 0 24 24" aria-hidden="true"><path d="M2 5h20v14H2z M3.5 6.5 12 13l8.5-6.5" stroke="var(--white)" stroke-width="1.5"/></svg>
        daniel@frost-haven-example.com
      </span>
    </div>
    <div class="row contact contact-line-2">
      <span class="contact-item">
        <svg class="contact-icon" viewBox="0 0 24 24" aria-hidden="true"><circle cx="12" cy="12" r="10"/><path d="M2 12h20M12 2c3 3 3 17 0 20M12 2c-3 3-3 17 0 20" fill="none" stroke="var(--white)" stroke-width="1.4"/></svg>
        www.frost-haven-example.com
      </span>
    </div>
  </div>
</section>

<section class="card card--back" aria-label="Business card back">
  <svg class="card-shape" width="668" height="380" viewBox="0 0 668 380" aria-hidden="true">
    <path d="M30,0 H638 A30,30 0 0 0 668,30 V350 A30,30 0 0 0 638,380 H30 A30,30 0 0 0 0,350 V30 A30,30 0 0 0 30,0 Z" fill="var(--white)"/>
    <path d="M33,5 H635 A30,30 0 0 0 663,33 V347 A30,30 0 0 0 635,375 H33 A30,30 0 0 0 5,347 V33 A30,30 0 0 0 33,5 Z" fill="var(--card-blue)"/>
  </svg>
  <div class="card-content">
    <div class="row company-name">Frost-Haven Company</div>
    <div class="row ruled-heading agreements">Maintenance agreements</div>
    <div class="row service-list provide"><span class="label">We provide :</span> Sales | Design | Installation | Service | Maintenance</div>
    <div class="row service-list service"><span class="label">We service :</span> Refrigeration | Heating | Air Conditioning | Ice Machines</div>
    <div class="row ruled-heading around-the-clock">24 Hour Service</div>
  </div>
</section>

</body>
</html>
```